Business Card Design

I already have a company logo for my company. I have a logo for the manufacturer we represent. I want a professional business card design.

```html
<!DOCTYPE html>
<html lang="en">
<head>
<meta charset="utf-8">
<title>Beacon Alert Group – Business Card</title>
<link rel="stylesheet" href="https://fonts.googleapis.com/css2?family=Montserrat:wght@600;800&family=Lato:wght@400;700&display=swap">
<style>
  :root {
    --bg: #2a2b2e;
    --card-dark: #1c1c1e;
    --card-light: #ffffff;
    --red: #e0202a;
    --gold: #e2a21a;
    --ink: #1a1a1a;
    --grey: #6b6b6b;
    --rule: #d9d9d9;
  }
  * { margin: 0; padding: 0; box-sizing: border-box; }
  html, body { width: 1200px; height: 952px; overflow: hidden; }
  body {
    background: var(--bg);
    font-family: "Lato", sans-serif;
    display: flex;
    align-items: center;
    justify-content: center;
    gap: 40px;
  }
  .card {
    width: 520px;
    height: 297px;
    position: relative;
    overflow: hidden;
    box-shadow: 0 18px 40px rgba(0,0,0,.45);
  }
  /* Front */
  .card-front {
    background: var(--card-dark);
    display: flex;
    align-items: center;
    justify-content: center;
  }
  .brand {
    display: flex;
    align-items: center;
    gap: 12px;
    font-family: "Montserrat", sans-serif;
    font-weight: 800;
    letter-spacing: .04em;
    line-height: 1.05;
    text-transform: uppercase;
  }
  .brand-mark {
    width: 16px;
    height: 16px;
    background: var(--red);
    flex: none;
  }
  .card-front .brand-name { color: #ffffff; font-size: 30px; }
  /* Back */
  .card-back { background: var(--card-light); }
  .tab {
    position: absolute;
    background: var(--ink);
  }
  .tab-top { left: 0; top: 38px; width: 78px; height: 14px; }
  .tab-bottom { right: 0; bottom: 0; width: 96px; height: 68px; }
  .back-brand {
    position: absolute;
    left: 40px;
    top: 96px;
    width: 190px;
  }
  .card-back .brand-name { color: var(--ink); font-size: 19px; }
  .divider {
    position: absolute;
    left: 252px;
    top: 92px;
    width: 1px;
    height: 120px;
    background: var(--rule);
  }
  .address {
    position: absolute;
    left: 40px;
    top: 236px;
    font-size: 9.5px;
    color: var(--grey);
  }
  .contact {
    position: absolute;
    left: 274px;
    top: 98px;
  }
  .person-name {
    font-family: "Montserrat", sans-serif;
    font-size: 17px;
    letter-spacing: .03em;
    text-transform: uppercase;
  }
  .first { color: var(--gold); font-weight: 600; }
  .last { color: var(--red); font-weight: 800; }
  .person-title { font-size: 11px; color: var(--grey); margin: 2px 0 14px; }
  .contact-list { list-style: none; }
  .contact-list li {
    display: flex;
    align-items: center;
    gap: 7px;
    font-size: 10.5px;
    color: var(--grey);
    margin-bottom: 5px;
  }
  .contact-list svg { width: 10px; height: 10px; fill: var(--ink); flex: none; }
</style>
</head>
<body>
  <section class="card card-front">
    <div class="brand">
      <span class="brand-mark"></span>
      <span class="brand-name">Beacon Alert<br>Group</span>
    </div>
  </section>

  <section class="card card-back">
    <span class="tab tab-top"></span>
    <span class="tab tab-bottom"></span>

    <div class="brand back-brand">
      <span class="brand-mark"></span>
      <span class="brand-name">Beacon Alert<br>Group</span>
    </div>
    <span class="divider"></span>
    <p class="address">1270 Harbor Crest Avenue Arlington, VA 22201</p>

    <div class="contact">
      <h1 class="person-name"><span class="first">Daniel R.</span> <span class="last">Hollis</span></h1>
      <p class="person-title">Managing Director</p>
      <ul class="contact-list">
        <li>
          <svg viewBox="0 0 10 10" aria-hidden="true"><path d="M2 0.5 L3.6 2.6 L2.8 3.6 Q4 6 6.4 7.2 L7.4 6.4 L9.5 8 L8.4 9.5 Q3.5 9 0.5 1.6 Z"/></svg>
          +00 555 210 34
        </li>
        <li>
          <svg viewBox="0 0 10 10" aria-hidden="true"><path d="M0 2 H10 V8 H0 Z M0.6 2.4 L5 5.6 L9.4 2.4 L9.4 3.2 L5 6.4 L0.6 3.2 Z" fill-rule="evenodd"/></svg>
          info@beaconalert.com
        </li>
        <li>
          <svg viewBox="0 0 10 10" aria-hidden="true"><path d="M5 0 A5 5 0 1 0 5.001 0 Z M5 1.2 A3.8 3.8 0 1 1 4.999 1.2 Z M3 3 Q5 4 4 6 Q6 6 7 8 Q8 5 6 3.5 Z" fill-rule="evenodd"/></svg>
          www.beaconalertgroup.com
        </li>
      </ul>
    </div>
  </section>
</body>
</html>
```